Business Card Design Project

I have attached the logo and the colour pallete for the branding for the company.

Creative designs for business cards are needed.

The Company is modern corporate.

Industry/Entity Type

Business

```html
<!DOCTYPE html>
<html lang="en">
<head>
<meta charset="utf-8">
<title>Pathnova Business Card</title>
<link rel="stylesheet" href="https://fonts.googleapis.com/css2?family=Questrial&display=swap">
<style>
  :root {
    --plum: #5a2159;
    --plum-light: #7a2d78;
    --plum-deep: #3f153f;
    --orange: #f08a2c;
    --white: #ffffff;
    --backdrop: #e9e7ea;
  }
  html, body {
    margin: 0;
    padding: 0;
    width: 1200px;
    height: 968px;
    overflow: hidden;
    background: var(--backdrop);
    font-family: "Questrial", "Century Gothic", sans-serif;
  }
  .canvas {
    position: relative;
    width: 1200px;
    height: 968px;
  }
  .card {
    position: absolute;
    left: 250px;
    width: 700px;
    height: 400px;
    box-shadow: 0 6px 18px rgba(0, 0, 0, 0.18);
    overflow: hidden;
  }
  .card-back { top: 60px; }
  .card-front { top: 508px; background: var(--white); }
  .card svg { display: block; width: 100%; height: 100%; }
  .brand-name {
    font-family: "Questrial", "Century Gothic", sans-serif;
    font-weight: 400;
  }
  .brand-name--light { fill: var(--white); font-size: 56px; }
  .brand-name--dark { fill: var(--plum); font-size: 58px; }
  .holder-name { fill: var(--plum); font-size: 32px; font-weight: 400; }
  .contact-line { fill: var(--white); font-size: 18px; }
</style>
</head>
<body>
<main class="canvas">

  <section class="card card-back" aria-label="Card back">
    <svg viewBox="0 0 700 400" xmlns="http://www.w3.org/2000/svg">
      <defs>
        <radialGradient id="back-glow" cx="0.55" cy="0.3" r="0.8">
          <stop offset="0" stop-color="var(--plum-light)"/>
          <stop offset="1" stop-color="var(--plum-deep)"/>
        </radialGradient>
      </defs>
      <rect class="back-fill" width="700" height="400" fill="url(#back-glow)"/>
      <text class="brand-name brand-name--light" x="120" y="250">pathnova</text>
    </svg>
  </section>

  <section class="card card-front" aria-label="Card front">
    <svg viewBox="0 0 700 400" xmlns="http://www.w3.org/2000/svg">
      <defs>
        <radialGradient id="front-band" cx="0.75" cy="0.7" r="0.8">
          <stop offset="0" stop-color="var(--plum-light)"/>
          <stop offset="1" stop-color="var(--plum-deep)"/>
        </radialGradient>
      </defs>
      <path class="accent-swoosh" d="M0,252 Q360,240 700,150 L700,164 Q360,256 0,268 Z" fill="var(--orange)"/>
      <path class="footer-band" d="M0,266 Q360,254 700,170 L700,400 L0,400 Z" fill="url(#front-band)"/>
      <text class="brand-name brand-name--dark" x="58" y="138">pathnova</text>
      <text class="holder-name" x="440" y="130">Daniel Reyes</text>
      <text class="contact-line" x="52" y="338">danielreyes@pathnova.com</text>
      <text class="contact-line" x="52" y="362">www.pathnova.com</text>
    </svg>
  </section>

</main>
</body>
</html>
```